Medical Billing Company needs Trifold Brochure Design

We do medical billing and consulting for all types of medical services including hospitals, clinics, physical therapy, mental health, and all other physician specialties. We want to attract new clients from all areas. This is what we have listed on our LinkedIn page: Korvath Billing and Consulting offers 128 years of combined medical billing, coding, credentialing, auditing, and practice management experience. Integrity, reliability, dedication, and open communication are the cornerstones of our foundation. We strive to create meaningful relationships with our clients so they may focus on what they do best, and allow us to handle the rest.

We understand the changes occurring in our healthcare system. Reimbursement is decreasing, expenses are increasing, and the dedication and tenacity to collect every dollar due from the carriers is vital to the financial health of the hospital or practitioner.

Target Market(s)

Physicians, hospitals and any other providers in the medical field such as durable medical equipment suppliers and mid-level providers

Font styles to use
Sans Serif

Colors

Designer to choose colors to be used in the design.

Requirements
Must have
• Specifics list of services we offer. List attached.

```html
<!DOCTYPE html>
<html lang="en">
<head>
<meta charset="utf-8">
<title>Korvath Billing and Consulting – Trifold Brochure</title>
<link href="https://fonts.googleapis.com/css2?family=Open+Sans:wght@400;600;700;800&family=Oswald:wght@400;500;600&display=swap" rel="stylesheet">
<style>
  :root{
    --tan:#a99a7b;
    --tan-dark:#8f8062;
    --beige:#ece7dc;
    --paper:#ffffff;
    --page:#f4f4f4;
    --green:#3b9f63;
    --accent:#d3892f;
    --ink:#4a4a4a;
    --muted:#8a8a8a;
  }
  *{box-sizing:border-box;margin:0;padding:0}
  html,body{width:849px;height:1200px;overflow:hidden;background:var(--page);font-family:"Open Sans",Arial,sans-serif;color:var(--ink)}
  .sheet{position:absolute;left:80px;width:690px;display:flex;box-shadow:0 6px 18px rgba(0,0,0,.25);background:var(--paper)}
  .sheet--outside{top:70px;height:510px}
  .sheet--inside{top:622px;height:496px}
  .panel{position:relative;width:230px;height:100%;overflow:hidden}
  .url{position:absolute;left:0;right:0;bottom:0;height:22px;line-height:22px;font-size:8px;color:#fff;padding-left:12px;letter-spacing:.3px}

  /* outside: services panel */
  .panel--services{background:var(--tan);color:#fff}
  .services__title{font-family:"Oswald",sans-serif;font-weight:500;font-size:17px;letter-spacing:.5px;margin:22px 0 8px 16px}
  .services__list{list-style:none;margin-left:16px;font-size:8.2px;font-weight:600;line-height:1.28;letter-spacing:.2px}
  .services__list li{position:relative;padding-left:10px;margin-bottom:2px;width:190px}
  .services__list li::before{content:"";position:absolute;left:0;top:3.5px;width:4px;height:4px;background:#fff;border-radius:50%}
  .services__photo{position:absolute;left:0;right:0;top:382px;height:106px;background:linear-gradient(135deg,#e8e6e1,#bdb6a8 55%,#7f7566)}
  .panel--services .url{background:var(--tan-dark)}

  /* outside: cover/contact panel */
  .panel--contact{background:var(--tan);color:#fff;border-left:1px solid rgba(255,255,255,.35);border-right:1px solid rgba(255,255,255,.35)}
  .brand{display:flex;align-items:center;gap:8px}
  .brand__square{width:22px;height:22px;background:currentColor}
  .brand__name{font-family:"Open Sans",sans-serif;font-weight:700;font-size:24px;letter-spacing:.5px}
  .brand__tag{font-size:7px;letter-spacing:1.5px;text-transform:uppercase;margin-top:2px}
  .panel--contact .brand-block{position:absolute;top:150px;left:30px}
  .address{position:absolute;top:245px;left:0;right:0;text-align:center;font-size:10px;line-height:1.45;letter-spacing:.4px;text-transform:uppercase}
  .phones{position:absolute;top:300px;left:0;right:0;text-align:center;font-size:10px;line-height:1.5;letter-spacing:.4px}
  .panel--contact .url{background:var(--tan-dark)}

  /* outside: front panel */
  .panel--front{background:var(--beige)}
  .front__photo{position:absolute;left:0;right:0;top:0;height:345px;background:linear-gradient(160deg,#f3f6f8,#cfd9df 50%,#9fb1bd)}
  .panel--front .brand-block{position:absolute;top:14px;right:14px;color:var(--green)}
  .panel--front .brand__name{font-size:20px}
  .panel--front .brand__square{width:18px;height:18px}
  .panel--front .brand__tag{color:var(--ink)}
  .headline{position:absolute;top:365px;right:16px;text-align:right;font-family:"Oswald",sans-serif;text-transform:uppercase}
  .headline__lead{color:var(--green);font-size:17px;font-weight:500;line-height:1.1}
  .headline__main{color:var(--tan);font-size:26px;font-weight:600;line-height:1.05}
  .panel--front .url{background:var(--tan)}

  /* inside */
  .inside__backdrop{position:absolute;inset:0;background:linear-gradient(135deg,#dfe2e4,#f3f1ec 45%,#c9c3b6)}
  .sheet--inside .panel{background:transparent}
  .card{position:absolute;left:14px;right:14px;top:48px;height:392px;background:var(--paper);box-shadow:0 2px 6px rgba(0,0,0,.15)}
  .card__heading{padding:16px 14px 10px;font-family:"Oswald",sans-serif;text-transform:uppercase;line-height:1.05}
  .card__pre{display:block;color:var(--muted);font-size:14px;font-weight:400}
  .card__word{display:block;color:var(--accent);font-size:18px;font-weight:500}
  .card__photo{height:90px;margin:0 10px;background:linear-gradient(135deg,#e9e7e2,#b7afa0 60%,#857b6b)}
  .card__body{position:absolute;left:10px;right:10px;top:168px;bottom:10px;background:var(--tan);color:#fff;padding:16px 12px;font-size:14px;line-height:1.35}
  .sheet--inside .url{background:rgba(143,128,98,.9)}
</style>
</head>
<body>

<section class="sheet sheet--outside">
  <div class="panel panel--services">
    <h2 class="services__title">SERVICES INCLUDE:</h2>
    <ul class="services__list">
      <li>ELECTRONIC &amp; PAPER CLAIMS</li>
      <li>INSURANCE FOLLOW UPS</li>
      <li>MONTHLY PATIENT BILLING</li>
      <li>PAYMENT POSTING</li>
      <li>COMPREHENSIVE MONTHLY REPORTS</li>
      <li>DENIAL MANAGEMENT INCLUDING APPEALS</li>
      <li>PAST DUE CLAIMS</li>
      <li>INSURANCE VERIFICATION</li>
      <li>AUTHORIZATION TRACKING</li>
      <li>PRACTICE CONSULTING</li>
      <li>REMOTE ACCESS CONSULTING</li>
      <li>TRACKING AND VERIFYING ALLOWABLES</li>
      <li>CREDENTIALING</li>
      <li>CLAIM CORRECTION AND RESUBMISSION</li>
      <li>EMERGENCY "FILL-IN" OR TRANSITION BILLING</li>
      <li>LET US WORK WHEN YOU CAN'T</li>
    </ul>
    <div class="services__photo" role="img" aria-label="Photo of hands working with a calculator and billing papers"></div>
    <div class="url">www.korvathbilling.example</div>
  </div>

  <div class="panel panel--contact">
    <div class="brand-block">
      <div class="brand"><span class="brand__square"></span><span class="brand__name">Korvath</span></div>
      <div class="brand__tag">Billing &amp; Consulting</div>
    </div>
    <p class="address">47 Larkspur Row<br>Alder Falls, NM 87990</p>
    <p class="phones">TEL: 505-014-2270<br>FAX: 505-014-2271</p>
    <div class="url">www.korvathbilling.example</div>
  </div>

  <div class="panel panel--front">
    <div class="front__photo" role="img" aria-label="Photo of a smiling doctor with a stethoscope"></div>
    <div class="brand-block">
      <div class="brand"><span class="brand__square"></span><span class="brand__name">Korvath</span></div>
      <div class="brand__tag">Billing &amp; Consulting</div>
    </div>
    <div class="headline">
      <div class="headline__lead">The best medicine</div>
      <div class="headline__main">For a broken<br>billing cycle</div>
    </div>
    <div class="url">www.korvathbilling.example</div>
  </div>
</section>

<section class="sheet sheet--inside">
  <div class="inside__backdrop" role="img" aria-label="Soft background photo of a desk with documents"></div>

  <div class="panel">
    <article class="card">
      <h3 class="card__heading"><span class="card__pre">Our</span><span class="card__word">Philosophy</span></h3>
      <div class="card__photo" role="img" aria-label="Photo of a person reviewing paperwork"></div>
      <p class="card__body">Our philosophy is simple, we are here to help you collect every dollar you've earned.</p>
    </article>
    <div class="url">www.korvathbilling.example</div>
  </div>

  <div class="panel">
    <article class="card">
      <h3 class="card__heading"><span class="card__pre">Our</span><span class="card__word">Services</span></h3>
      <div class="card__photo" role="img" aria-label="Photo of hands with a calculator and charts"></div>
      <p class="card__body">Fewer headaches, more profitability and we can prove it!</p>
    </article>
    <div class="url">www.korvathbilling.example</div>
  </div>

  <div class="panel">
    <article class="card">
      <h3 class="card__heading"><span class="card__pre">Our</span><span class="card__word">Experience</span></h3>
      <div class="card__photo" role="img" aria-label="Photo of professionals in a meeting"></div>
      <p class="card__body">We bring certified professionals from a variety of medical backgrounds to serve you.</p>
    </article>
    <div class="url">www.korvathbilling.example</div>
  </div>
</section>

</body>
</html>
```